依頼概要
10月から始める、動物病院の健康診断キャンペーンのDM(ハガキ)のデザインをお願いします

以前、作成したDMを載せておきますので参考にしていただければと思います

必ず入れていただきたい項目(文言はお任せします)
・対象動物:ワンちゃん ネコちゃん ウサギさん
・キャンペーン期間:10月1日から11月30日まで
・キャンペーン内容:
一般健康診断(身体検査、血液検査(血球検査+生化学検査19項目))通常9000が6000円
オプション検査(尿検査、糞便検査、ホルモン検査(甲状腺など)、レントゲン検査、エコー検査)各30%OFF
・エコー検査は電話にて予約が必要
・できれば12時間絶食で来院
・下部に病院の情報

表面(宛名面)
以前と同様に下部に
秋の健康診断キャンペーンの案内
病院の情報(診療時間など)

カミテックさんのポストカード印刷のアートポスト180kg両面印刷でお願いする予定です。
規格はそちらに合わせていただければと思います。

シンプルで分かりやすいものを希望しています。
きっかりしているものよりも、秋らしい雰囲気なもの、可愛らしいものを希望します。

お手数ですが、診療時間などの詳細はHPよりお願いします。
https://www.sorano-vet.example
申し訳ございません
病院のロゴデータを添付し忘れましたので添付しておきます。
よろしくお願いします。
以前のDMデータです
■ 選んだ理由

わかりやすく、かわいらしいデザインで老若男女問わず親しみやすいデザインだったため。

■ 提案者全員のお礼・コメント

このたびは素敵なご提案をたくさんいただきありがとうございます。
どれも甲乙つけがたく、デザインをみさせてもらうのが楽しかったです。
スタッフのアンケートで多数だったものを今回は選ばせていただきました。
また機会がありましたらよろしくお願いいたします。

```html
<!DOCTYPE html>
<html lang="ja">
<head>
<meta charset="UTF-8">
<title>秋の健康診断キャンペーン</title>
<link href="https://fonts.googleapis.com/css2?family=Zen+Maru+Gothic:wght@500;700;900&display=swap" rel="stylesheet">
<style>
:root{
  --cream:#fbf2df;
  --brown:#5b3a1f;
  --orange:#ef8a1e;
  --navy:#1d3d6e;
  --teal:#2f9ea0;
  --pink:#e7869c;
  --red:#e23b3b;
  --ink:#333;
  --white:#fff;
}
*{margin:0;padding:0;box-sizing:border-box}
html,body{width:811px;height:1200px;overflow:hidden;background:var(--cream)}
body{font-family:"Zen Maru Gothic",sans-serif;color:var(--ink)}
.card{position:relative;width:811px;height:1200px;background:var(--cream);overflow:hidden}
.abs,.art{position:absolute}
.title-line{color:var(--brown);font-weight:900;font-size:56px;letter-spacing:4px;line-height:1;white-space:nowrap}
.title-1{left:176px;top:62px}
.title-2{left:286px;top:132px}
.badge{left:36px;top:190px;width:230px;height:74px;background:#fffbe9;border:3px solid var(--red);border-radius:14px;transform:rotate(-6deg);color:var(--red);font-weight:700;font-size:20px;line-height:1.35;text-align:center;padding-top:5px;white-space:nowrap}
.badge small{font-size:16px}
.period{left:0;top:252px;width:811px;text-align:center;color:var(--orange);font-weight:900;font-size:38px;line-height:1}
.dates{left:0;top:300px;width:811px;text-align:center;color:var(--navy);font-weight:900;font-size:54px;line-height:1;white-space:nowrap}
.panel{left:108px;width:600px;background:var(--white);border-radius:10px;overflow:hidden}
.panel-head{height:48px;color:var(--white);font-weight:900;font-size:32px;text-align:center;line-height:48px;letter-spacing:3px}
.general{top:380px;height:216px;border:3px solid var(--teal)}
.general .panel-head{background:var(--teal)}
.options{top:614px;height:190px;border:3px solid var(--pink)}
.options .panel-head{background:var(--pink)}
.item{font-size:27px;font-weight:700;color:var(--ink);padding-left:36px;line-height:38px;white-space:nowrap}
.items{padding-top:16px}
.price{margin:8px 30px 0;border-top:2px dashed #bbb;padding-top:10px;font-size:26px;font-weight:700;color:var(--red);line-height:44px;white-space:nowrap}
.price s{color:var(--ink);text-decoration-color:var(--red)}
.price b{font-size:38px;font-weight:900}
.off{left:618px;top:688px;width:160px;height:160px;border-radius:50%;background:var(--orange);color:var(--white);text-align:center;font-weight:900;line-height:1}
.off .k{display:block;font-size:26px;padding-top:24px}
.off .n{display:block;font-size:56px;padding-top:4px}
.off .o{display:block;font-size:30px;padding-top:2px}
.note-head{left:0;top:862px;width:811px;text-align:center;color:var(--brown);font-size:22px;font-weight:700;line-height:1}
.note{left:108px;top:896px;width:600px;height:96px;background:var(--white);border:3px solid var(--teal);border-radius:10px;font-size:24px;font-weight:700;line-height:36px;padding:9px 24px;white-space:nowrap}
.foot{left:0;top:1020px;width:811px;height:180px;background:var(--white)}
.foot-lead{right:40px;top:18px;font-size:22px;font-weight:700;color:var(--ink)}
.brand{left:30px;top:66px;display:flex;align-items:center;gap:12px;color:var(--navy);font-weight:700}
.brand-dot{width:40px;height:40px;border-radius:50%;background:var(--teal)}
.brand-name{font-size:28px;line-height:1.1}
.brand-name span{display:block;font-size:13px;letter-spacing:1px}
.url{right:40px;top:62px;font-size:20px;font-weight:700}
.search{right:40px;top:112px;display:flex;align-items:center;gap:10px;font-size:20px;font-weight:700}
.search-box{border:2px solid #888;border-radius:4px;padding:2px 12px;display:flex;align-items:center;gap:8px}
</style>
</head>
<body>
<div class="card">
  <div class="art" role="img" aria-label="紅葉とどんぐりの飾り" style="left:0;top:0;width:110px;height:110px;background:radial-gradient(circle,#d9823a 0%,rgba(217,130,58,0) 70%)"></div>
  <div class="art" role="img" aria-label="犬と猫のイラスト" style="left:560px;top:14px;width:230px;height:220px;border-radius:40%;background:radial-gradient(circle at 50% 50%,#e9c48a 0%,#d9c0a0 55%,rgba(217,192,160,0) 75%)"></div>
  <div class="art" role="img" aria-label="紅葉の飾り" style="left:470px;top:150px;width:110px;height:110px;background:radial-gradient(circle,#e58a3a 0%,rgba(229,138,58,0) 70%)"></div>
  <div class="art" role="img" aria-label="紅葉とどんぐりの飾り" style="left:0;top:380px;width:100px;height:180px;background:radial-gradient(circle,#e39a3e 0%,rgba(227,154,62,0) 70%)"></div>
  <div class="art" role="img" aria-label="紅葉とどんぐりの飾り" style="left:712px;top:380px;width:100px;height:180px;background:radial-gradient(circle,#d6703a 0%,rgba(214,112,58,0) 70%)"></div>

  <h1>
    <span class="abs title-line title-1">秋の健康診断</span>
    <span class="abs title-line title-2">キャンペーン</span>
  </h1>
  <div class="abs badge">ワンちゃん・ネコちゃん<br>ウサギさん <small>対象</small></div>

  <p class="abs period">キャンペーン期間</p>
  <p class="abs dates">10月1日〜11月30日まで</p>

  <section class="abs panel general">
    <h2 class="panel-head">一般健康診断</h2>
    <div class="items">
      <p class="item">身体検査＋血液検査</p>
      <p class="item">(血球検査＋生化学検査19項目)</p>
    </div>
    <p class="price"><s>通常9,000円</s> ▶▶▶ <b>6000円</b></p>
  </section>

  <section class="abs panel options">
    <h2 class="panel-head">オプション検査</h2>
    <div class="items">
      <p class="item">尿検査・糞便検査</p>
      <p class="item">ホルモン検査(甲状腺など)</p>
      <p class="item">レントゲン検査・エコー検査</p>
    </div>
  </section>
  <div class="abs off"><span class="k">各種</span><span class="n">30%</span><span class="o">OFF</span></div>

  <p class="abs note-head">〜ご来院されるお客様へお願い〜</p>
  <div class="abs note">
    <p>エコー検査は電話にて予約が必要になります。</p>
    <p>できれば12時間絶食で来院をお願いします。</p>
  </div>

  <footer class="abs foot">
    <p class="abs foot-lead">詳しくはHPをご覧ください。</p>
    <div class="abs brand">
      <div class="brand-dot"></div>
      <div class="brand-name">空野どうぶつクリニック<span>SORANO ANIMAL CLINIC</span></div>
    </div>
    <p class="abs url">https://www.sorano-vet.example</p>
    <div class="abs search">または
      <div class="search-box">
        <svg width="20" height="20" viewBox="0 0 20 20"><circle cx="8" cy="8" r="6" fill="none" stroke="#555" stroke-width="2.5"/><line x1="12.5" y1="12.5" x2="18" y2="18" stroke="#555" stroke-width="2.5"/></svg>
        空野 どうぶつクリニック
      </div>
    </div>
  </footer>
</div>
</body>
</html>
```